RLT Nursing Care

I am a registered nurse with a private nursing care service.
We provide the following care;
Registered Nursing, Palliative Nursing, personal care, dementia repite, day respite , overnight respite, domestic assistance, welfare checks, and transport.
In the community, our service is brochured by service providers and we also supply to private clients.

Target Market(s)

Aged care, disabled clients, dementia clients in the community

Industry/Entity Type

Nurse

Font styles to use
Sans Serif

Colors
6b449b
e44699
b868aa

Requirements
Must have
• Contact: Marlene Hobbs - Registered Nurse
PO Box 482 Dubbo
0437 215 608
Nice to have
• A soft caring picture feature

```html
<!DOCTYPE html>
<html lang="en">
<head>
<meta charset="utf-8">
<title>RLT Nursing Care – Flyer</title>
<link rel="stylesheet" href="https://fonts.googleapis.com/css2?family=Jost:wght@400;500;600;700&display=swap">
<style>
  :root {
    --pink: #e44699;
    --purple: #6b449b;
    --mauve: #b868aa;
    --white: #ffffff;
    --ink: #111111;
    --backdrop: #e6e7e9;
    --panel-grey: #f2f2f2;
  }
  * { margin: 0; padding: 0; box-sizing: border-box; }
  html, body {
    width: 927px; height: 1200px; overflow: hidden;
    background: var(--backdrop);
    font-family: "Jost", "Helvetica Neue", Arial, sans-serif;
  }
  .card {
    position: absolute;
    width: 640px; height: 480px;
    left: 143px;
    background: var(--pink);
    overflow: hidden;
  }
  .card--front { top: 70px; }
  .card--back { top: 640px; }
  .card__art { position: absolute; inset: 0; }

  .front__title {
    position: absolute; left: 30px; top: 28px;
    color: var(--white); font-weight: 700; font-size: 34px;
    letter-spacing: 0.5px; white-space: nowrap;
  }
  .front__intro {
    position: absolute; left: 40px; top: 84px;
    color: var(--white); font-weight: 500; font-size: 17px; line-height: 1.2;
  }
  .services {
    position: absolute; left: 36px; top: 234px;
    color: var(--ink);
  }
  .services__heading { font-weight: 600; font-size: 17px; margin-bottom: 6px; }
  .services__list { list-style: none; font-size: 15px; line-height: 1.5; }
  .services__list .dot { font-size: 12px; margin-right: 4px; }

  .front__note {
    position: absolute; left: 40px; top: 430px; width: 400px;
    color: var(--white); font-weight: 500; font-size: 13.5px; line-height: 1.25;
  }
  .contact {
    position: absolute; left: 452px; top: 352px;
    border-left: 1.5px solid var(--white);
    padding: 2px 0 14px 14px;
    color: var(--white); line-height: 1.25;
    font-style: normal;
  }
  .contact__name { font-weight: 600; font-size: 16px; }
  .contact__role { font-size: 15px; margin-bottom: 10px; }
  .contact__detail { font-size: 15px; }

  .back__panel {
    position: absolute; left: 360px; top: 190px;
    width: 235px; height: 190px;
    background: var(--panel-grey); border-radius: 24px;
    color: var(--pink); text-align: center;
    padding-top: 26px;
    font-style: normal;
  }
  .back__name { font-weight: 600; font-size: 21px; line-height: 1.1; }
  .back__role { font-size: 19px; line-height: 1.2; }
  .back__rule {
    position: relative; width: 130px; height: 2px; background: var(--pink);
    margin: 12px auto 14px;
  }
  .back__rule::before, .back__rule::after {
    content: ""; position: absolute; top: -2.5px;
    width: 7px; height: 7px; border-radius: 50%; background: var(--pink);
  }
  .back__rule::before { left: -3px; }
  .back__rule::after { right: -3px; }
  .back__detail { font-size: 19px; line-height: 1.2; }
</style>
</head>
<body>

<section class="card card--front">
  <svg class="card__art" viewBox="0 0 640 480" width="640" height="480">
    <defs>
      <clipPath id="band-clip">
        <path d="M0,218 C160,250 300,205 420,150 S590,100 640,98 L640,282 C560,270 460,310 360,360 S120,412 0,392 Z"/>
      </clipPath>
      <linearGradient id="photo-tone" x1="0" y1="0" x2="1" y2="0">
        <stop offset="0" stop-color="#eef1f4"/>
        <stop offset="0.35" stop-color="#7fa8cf"/>
        <stop offset="0.7" stop-color="#e9e6e2"/>
        <stop offset="1" stop-color="#f7f7f7"/>
      </linearGradient>
    </defs>
    <path fill="#ffffff" d="M0,218 C160,250 300,205 420,150 S590,100 640,98 L640,282 C560,270 460,310 360,360 S120,412 0,392 Z"/>
    <g role="img" aria-label="Photo of a nurse gently helping an elderly woman walk" clip-path="url(#band-clip)">
      <rect x="345" y="90" width="295" height="280" fill="url(#photo-tone)"/>
    </g>
    <path fill="none" stroke="#6b449b" stroke-width="4" d="M0,210 C160,242 300,197 420,142 S590,92 640,90"/>
    <path fill="none" stroke="#6b449b" stroke-width="4" d="M0,400 C120,420 260,418 360,368 S560,278 640,290"/>
  </svg>

  <h1 class="front__title">PRIVATE NURSING CARE SERVICE</h1>
  <p class="front__intro">I am a registered nurse with<br>a private nursing care service.</p>

  <div class="services">
    <h2 class="services__heading">WE PROVIDE THE FOLLOWING CARE</h2>
    <ul class="services__list">
      <li><span class="dot">◆</span>Registered Nursing <span class="dot">◆</span>Palliative Nursing</li>
      <li><span class="dot">◆</span>personal care <span class="dot">◆</span>dementia repite</li>
      <li><span class="dot">◆</span>day respite <span class="dot">◆</span>overnight respite</li>
      <li><span class="dot">◆</span>domestic assistance</li>
      <li><span class="dot">◆</span>welfare checks, and transport.</li>
    </ul>
  </div>

  <p class="front__note">In the community, our service is brochured by service providers and we also supply to private clients.</p>

  <address class="contact">
    <p class="contact__name">MARLENE HOBBS</p>
    <p class="contact__role">Registered Nurse</p>
    <p class="contact__detail">PO Box 482 Dubbo</p>
    <p class="contact__detail">0437 215 608</p>
  </address>
</section>

<section class="card card--back">
  <address class="back__panel">
    <p class="back__name">MARLENE HOBBS</p>
    <p class="back__role">Registered Nurse</p>
    <div class="back__rule"></div>
    <p class="back__detail">PO Box 482 Dubbo</p>
    <p class="back__detail">0437 215 608</p>
  </address>
</section>

</body>
</html>
```